Motor Mate 4x6 Flyer

Need 4 x 6 Flyer with following language:

Willow Crest Motor Mate
Our Motor Mate Will Come to Your Home
Our Motor Mate will Drive Your Car to Nearest Gas Station
Our Motor Mate will Fill-up Your Car with Gas
Our Motor Mate will Immediately Return Your Car
Your Car Covered with $100k of Commercial Insurance
Member Dunmore Chamber of Commerce / Honest Merchant League
www.willowcrestmotormate.example

Place logos of Vortan, Brenn & Dorvane on Left Side of Flyer starting at top left corner, mid left side, left bottom corner.
Place logos of BoltNest, 12-Forty, Tesmira on opposite side right.....
Place Willow Crest Motor Mate Logo on both sides of very top that says Willow Crest Motor Mate

Target Market(s)

Upscale Home Owners

Font styles to use
Sans Serif

Colors
F0912C
F2A743
F7CA91
FBE8D2
FDF5EE

Requirements
Must have
• Flyer Must be Bright Orange

```html
<!DOCTYPE html>
<html lang="en">
<head>
<meta charset="utf-8">
<title>Willow Crest Motor Mate Flyer</title>
<link href="https://fonts.googleapis.com/css2?family=Montserrat:wght@500;600;700;800;900&family=Dancing+Script:wght@700&display=swap" rel="stylesheet">
<style>
  :root {
    --orange: #F0912C;
    --orange-mid: #F2A743;
    --orange-soft: #F7CA91;
    --cream: #FBE8D2;
    --ivory: #FDF5EE;
    --red: #E3262B;
    --red-dark: #B81A1F;
    --ink: #2B2B2B;
    --white: #FFFFFF;
  }
  * { box-sizing: border-box; margin: 0; padding: 0; }
  html, body { width: 874px; height: 1200px; overflow: hidden; background: var(--white); }
  body { font-family: "Montserrat", Arial, sans-serif; color: var(--ink); }
  .flyer { position: relative; width: 874px; height: 1200px; background: var(--white); overflow: hidden; }

  .brand-mark { position: absolute; left: 58px; top: 42px; display: flex; flex-direction: column; align-items: flex-start; gap: 10px; }
  .brand-mark .mark-square { width: 64px; height: 64px; border: 5px solid var(--red); border-radius: 8px; }
  .brand-mark .mark-name { font-weight: 800; font-size: 34px; color: var(--red); letter-spacing: 1px; text-transform: uppercase; }

  .fuel-partners { position: absolute; left: 58px; top: 196px; display: flex; gap: 22px; align-items: center; }
  .partner-name { font-weight: 800; font-size: 22px; color: var(--red); text-transform: uppercase; white-space: nowrap; }

  .nozzle-art { position: absolute; right: 40px; top: 0; width: 340px; height: 330px;
    background: linear-gradient(160deg, #d9d9d9 0%, #9a9a9a 45%, var(--red) 75%, var(--red-dark) 100%);
    border-radius: 0 0 40px 160px; opacity: .9; }

  .paint-splash { position: absolute; left: 0; top: 250px; width: 874px; height: 820px;
    background: linear-gradient(180deg, var(--orange-soft) 0%, var(--orange-mid) 25%, var(--orange) 60%, var(--orange-mid) 100%);
    clip-path: polygon(0 14%, 20% 6%, 45% 10%, 70% 2%, 100% 8%, 100% 96%, 70% 100%, 40% 95%, 0 100%); }

  .headline { position: absolute; left: 0; top: 400px; width: 874px; text-align: center; }
  .headline .place { font-weight: 900; font-size: 72px; color: var(--white); letter-spacing: 1px; line-height: 1; text-transform: uppercase; text-shadow: 0 3px 6px rgba(0,0,0,.15); }
  .headline .service { display: inline-block; margin-top: 14px; background: var(--red); color: var(--white); font-weight: 900; font-size: 66px; line-height: 1; padding: 12px 34px; text-transform: uppercase; }
  .tagline { position: absolute; left: 0; top: 610px; width: 874px; text-align: center; font-family: "Dancing Script", cursive; font-size: 58px; color: var(--white); }

  .promises { position: absolute; left: 92px; top: 704px; width: 690px; display: grid; grid-template-columns: 1fr 1fr; gap: 22px 30px; list-style: none; }
  .promise { display: flex; align-items: center; gap: 16px; background: var(--white); height: 86px; padding: 0 14px; box-shadow: 0 4px 10px rgba(0,0,0,.12); }
  .promise .icon { flex: 0 0 84px; height: 58px; background: var(--red); border-radius: 4px; display: flex; align-items: center; justify-content: center; }
  .promise .icon svg { width: 34px; height: 34px; }
  .promise .text { font-weight: 600; font-size: 20px; line-height: 1.2; color: var(--ink); }

  .footer-band { position: absolute; left: 0; bottom: 0; width: 874px; height: 150px; background: var(--white);
    clip-path: polygon(0 18%, 15% 8%, 35% 16%, 55% 4%, 78% 14%, 100% 6%, 100% 100%, 0 100%); }
  .web-address { position: absolute; left: 48px; bottom: 48px; display: flex; align-items: center; gap: 10px; font-weight: 700; font-size: 19px; color: var(--ink); white-space: nowrap; }
  .retail-partners { position: absolute; right: 40px; bottom: 48px; display: flex; gap: 16px; align-items: center; }
  .retail-partners .partner-name { font-size: 17px; }
</style>
</head>
<body>
<main class="flyer">
  <div class="paint-splash" role="img" aria-label="Bright orange paint splash background"></div>
  <div class="nozzle-art" role="img" aria-label="Red fuel pump nozzle with hose"></div>

  <header class="brand-mark">
    <span class="mark-square"></span>
    <span class="mark-name">Motor Mate</span>
  </header>

  <div class="fuel-partners">
    <span class="partner-name">Vortan</span>
    <span class="partner-name">Brenn</span>
    <span class="partner-name">Dorvane</span>
  </div>

  <section class="headline">
    <h1 class="place">Willow Crest</h1>
    <div class="service">Motor Mate</div>
  </section>
  <p class="tagline">Our Motor Mate Will</p>

  <ul class="promises">
    <li class="promise">
      <span class="icon"><svg viewBox="0 0 24 24" fill="none" stroke="#fff" stroke-width="2"><path d="M2 15h13V7H2zM15 10h4l3 3v2h-7"/><circle cx="6" cy="17" r="2" fill="#fff"/><circle cx="18" cy="17" r="2" fill="#fff"/></svg></span>
      <span class="text">Come to<br>Your Home</span>
    </li>
    <li class="promise">
      <span class="icon"><svg viewBox="0 0 24 24" fill="none" stroke="#fff" stroke-width="2"><rect x="4" y="3" width="10" height="18" rx="1"/><path d="M6 7h6M14 9l4 3v6a1.5 1.5 0 0 0 3 0V8l-3-3"/></svg></span>
      <span class="text">Fill-up Your<br>Car with Gas</span>
    </li>
    <li class="promise">
      <span class="icon"><svg viewBox="0 0 24 24" fill="none" stroke="#fff" stroke-width="2"><circle cx="12" cy="12" r="9"/><circle cx="12" cy="12" r="2"/><path d="M3 12h7M14 12h7M12 14v7"/></svg></span>
      <span class="text">Drive Your Car to<br>Nearest Gas Station</span>
    </li>
    <li class="promise">
      <span class="icon"><svg viewBox="0 0 24 24" fill="none" stroke="#fff" stroke-width="2"><path d="M12 2l8 3v6c0 5-3.5 9-8 11-4.5-2-8-6-8-11V5z"/><path d="M8 12l3 3 5-6"/></svg></span>
      <span class="text">$100k of Commercial<br>Insurance</span>
    </li>
    <li class="promise">
      <span class="icon"><svg viewBox="0 0 24 24" fill="none" stroke="#fff" stroke-width="2"><path d="M4 8h14l-3-3M20 16H6l3 3"/></svg></span>
      <span class="text">Immediately<br>Return Your Car</span>
    </li>
    <li class="promise">
      <span class="icon"><svg viewBox="0 0 24 24" fill="none" stroke="#fff" stroke-width="2"><path d="M7 11v9H3v-9zM7 11l4-8a2 2 0 0 1 3 2v4h5a2 2 0 0 1 2 2l-2 7a2 2 0 0 1-2 2H7"/></svg></span>
      <span class="text">Honest Merchant<br>League</span>
    </li>
  </ul>

  <footer>
    <div class="footer-band"></div>
    <div class="web-address">
      <svg width="22" height="22" viewBox="0 0 24 24" fill="#E3262B"><path d="M4 3l16 7-7 2-2 7z"/></svg>
      www.willowcrestmotormate.example
    </div>
    <div class="retail-partners">
      <span class="partner-name">Tesmira</span>
      <span class="partner-name">BoltNest</span>
      <span class="partner-name">12-Forty</span>
    </div>
  </footer>
</main>
</body>
</html>
```